Internal Office Slogans / Motto / Vision Statements

Hi. We would like to put up some posters around the office with quotations such as -
-”Do what you do so well that they will want to see it again and bring their friends.”- Hollis Trevane
-Make your customers feel heard and understood. Make your customers feel respected and liked. Make your customers feel appreciated and helped. Understand that you can do none of these things unless you are sincere about them.
Gregory Pilcott
- It’s a very predictable and satisfying phenomenon: whenever we get better, our customers do too.
Ray Casso
-Catch people in the act of performing extraordinary customer service. Treat them like heroes. Tell their stories, far and wide.
Tod Brinkerley

The purpose of the posters is to reiterate our culture and vision within the organisation. They should be clean, crisp and eye catching, not gaudy or bright. Professional, bold and strong.

The company website and logo is at http://www.nexolux.com.au
Print size will be A1

Thanks for participating & looking forward to seeing your great work.
Updates

Hi All. . 

So to reiterate we are looking for one background design to be used for multiple quotes...  The list of quotes are as follows: 

Support and or Sales Office

 

Make your customers feel heard and understood.Make your customers feel respected and liked. Make your customers feelappreciated and helped. Understand that you can do none of these things unlessyou are sincere about them.

Gregory Pilcott

 

Nothing liberates our greatness like the desireto help, the desire to serve

Rosalind Penhallow

 

It’s a very predictable and satisfying phenomenon:whenever we get better, our customers do too.

Ray Casso

 

Success means we go to sleep at night knowingthat our talents and abilities were used in a way that served others.

Rosalind Penhallow.

 

The sole purpose of business is to create, serveand satisfy a customer, from beginning to end – and that’s everyone’s job.

Tod Brinkerley

 

We don’t celebrate closing a sale, we celebrateopening a relationship.

Gwendolyn Asque

I will never make you a promise – unless I giveyou a plan and procedure to make that promise possible.

Bo Tarrick

 

Customers feel we take them for granted; onlyshow interest when we want an order; lavish our time on prospects; communicatemainly by invoice; are fixated on big accounts; drop them like hot potatoesonce we have the order; don’t follow through on promises; and satisfy our ownbureaucracy rather than their needs. We can do better than that, much better.

Peter L Osmund.

 

 

General and public area

 

Catch people in the act of performingextraordinary customer service. Treat them like heroes. Tell their stories, farand wide.

Tod Brinkerley

 

 

We see our customers as invited guests to aparty, and we are the hosts. It’s our job every day to make every importantaspect of the customer experience a little bit better." Carl Ingvold - Founder andCEO of Veltrix

 

"If you do build a great experience,customers tell each other about that. Word of mouth is verypowerful."  Carl Ingvold

 

It's not a faithin technology. It's faith in people. Neil Corrby

 

“Being the richest man in the cemetery doesn’tmatter to me … Going to bed at night saying we’ve done something wonderful…that’s what matters to me.” Neil Corrby

 

The customer experience is the next competitivebattleground. Lance Merriwether, CIO, Quorra Computers

 

”Do what you do so well that they will want tosee it again and bring their friends.”- Hollis Trevane

In the world of internet customer service, it isimportant to remember your competitor is only a mouse click away. GlenTrasky (not sure who he is but like the quote).

The customer is why you go to work. If they goaway, you do, too. Martin Glossop (?)

 

MaybeSome for Sales or Build Team:

Quality is remembered long after the price is forgotten. Varenne Family Slogan

```html
<!DOCTYPE html>
<html lang="en">
<head>
<meta charset="utf-8">
<title>Nexolux – Customer Motto Poster</title>
<link rel="stylesheet" href="https://fonts.googleapis.com/css2?family=Anton&family=Arimo:wght@700&display=swap">
<style>
  :root {
    --ink: #000000;
    --signal-red: #c8000a;
    --mist: #e2e2e2;
    --white: #ffffff;
  }
  html, body {
    margin: 0;
    padding: 0;
    overflow: hidden;
    background: var(--white);
  }
  .poster {
    position: relative;
    width: 848px;
    height: 1200px;
    overflow: hidden;
    background: var(--ink);
  }
  .dial-backdrop {
    position: absolute;
    inset: 0;
  }
  .masthead {
    position: absolute;
    left: 0;
    top: 0;
    width: 848px;
    height: 237px;
    background: var(--ink);
    display: flex;
    align-items: center;
    justify-content: center;
  }
  .brand-name {
    margin: 0;
    font-family: "Arimo", Arial, sans-serif;
    font-weight: 700;
    font-size: 200px;
    line-height: 1;
    letter-spacing: -4px;
    color: var(--white);
    padding-top: 10px;
  }
  .motto-list {
    position: absolute;
    left: 22px;
    top: 264px;
    margin: 0;
    padding: 0;
    list-style: none;
    font-family: "Anton", Impact, sans-serif;
    font-size: 56px;
    line-height: 70px;
    letter-spacing: 0.2px;
  }
  .motto-list li {
    padding-left: 32px;
    text-indent: -32px;
  }
  .motto-light { color: var(--mist); }
  .motto-dark { color: var(--ink); }
  .attribution {
    position: absolute;
    left: 88px;
    top: 990px;
    margin: 0;
    font-family: "Anton", Impact, sans-serif;
    font-size: 76px;
    line-height: 1;
    color: var(--mist);
  }
</style>
</head>
<body>
<main class="poster">
  <svg class="dial-backdrop" width="848" height="1200" viewBox="0 0 848 1200" aria-hidden="true">
    <path d="M0 237 H848 V860 C800 1000 700 1120 585 1200 H0 Z" fill="var(--signal-red)"/>
    <line x1="590" y1="937" x2="790" y2="1120" stroke="var(--ink)" stroke-width="20"/>
    <circle cx="590" cy="937" r="40" fill="var(--ink)"/>
  </svg>

  <header class="masthead">
    <h1 class="brand-name">Nexolux</h1>
  </header>

  <ul class="motto-list">
    <li class="motto-light">- Make your customers feel<br>heard and understood.</li>
    <li class="motto-dark">- Make your customers feel<br>respected and liked.</li>
    <li class="motto-light">- Make your customers feel<br>appreciated and helped.</li>
    <li class="motto-dark">- Understand that you can<br>do none of these things<br>unless you are sincere<br>about them."</li>
  </ul>

  <p class="attribution">- Gregory Pilcott</p>
</main>
</body>
</html>
```